Shopwindow Design SHOW THE SYNERGY

create a shop-window for two startups under one roof. We have two company logos and specialize in two different fields; alkaline ionized water and ionizers and CBD enriched beverages and oils. please check our websites! brivelta.ch mendoli.swiss There is a great synergy between healthy ionized water and the benefits of CBD. We want the window to display this Synergy. We need the design to be "clean", professional, not like a stoner headshop! Display the seriousness and healthy sides of the businesses. Closer to Pharma style. - anti-inflammatory - anti-aging - alkalizing - anti-oxidant - improved focus - immune-support Perfomance boosting - detoxifying - hydrating - watersoluble CBD - sleep inducing - anxiolytic (anti anxiaty) - skin improvement - stress relieving - neuroprotective (neuroprotective) * please find shopwindow dimensions attached in pictures * we have two lightpanels (dimensions attached

```html
<!DOCTYPE html>
<html lang="de">
<head>
<meta charset="utf-8">
<title>Brivelta &amp; Mendoli – Schaufenster</title>
<link rel="stylesheet" href="https://fonts.googleapis.com/css2?family=Mulish:wght@400;500;600&display=swap">
<style>
  :root {
    --paper: #ffffff;
    --water-deep: #1f4f86;
    --water-mid: #4f8fc4;
    --water-light: #cfe8f3;
    --water-pale: #eaf5fa;
    --ink-navy: #23374a;
    --ink-cyan: #3ee0de;
    --ink-teal: #3aa8b8;
    --ink-green: #4a7d1e;
    --ink-brown: #5a3a1a;
    --leaf-green: #7fb23a;
  }
  html, body {
    margin: 0;
    padding: 0;
    overflow: hidden;
    background: var(--paper);
  }
  .window-panel {
    position: relative;
    width: 1200px;
    height: 613px;
    overflow: hidden;
    background: var(--paper);
    font-family: "Mulish", sans-serif;
  }
  .water-scene {
    position: absolute;
    left: 0;
    top: 0;
    width: 1200px;
    height: 613px;
  }
  .brand {
    position: absolute;
    line-height: 1;
    margin: 0;
  }
  .brand--water {
    left: 328px;
    top: 38px;
    font-size: 38px;
    font-weight: 600;
    color: var(--ink-navy);
    letter-spacing: -0.5px;
  }
  .brand--cbd {
    left: 624px;
    top: 12px;
    width: 112px;
    height: 112px;
    border: 3px solid var(--ink-brown);
    border-radius: 50%;
    display: flex;
    align-items: center;
    justify-content: center;
    font-size: 19px;
    font-weight: 600;
    color: var(--ink-brown);
    background: var(--paper);
  }
  .benefit {
    position: absolute;
    margin: 0;
    line-height: 1;
    white-space: nowrap;
    font-weight: 500;
  }
  .benefit--detox   { left: 48px;  top: 280px; font-size: 29px; color: var(--ink-cyan); }
  .benefit--cbd     { left: 92px;  top: 350px; font-size: 42px; color: var(--ink-green); font-weight: 600; letter-spacing: 0.5px; }
  .benefit--aging   { left: 70px;  top: 422px; font-size: 24px; color: var(--ink-teal); }
  .benefit--perform { left: 366px; top: 448px; font-size: 13px; color: var(--ink-brown); }
  .benefit--inflam  { left: 92px;  top: 498px; font-size: 29px; color: var(--ink-cyan); }
  .benefit--hydrate { left: 656px; top: 328px; font-size: 22px; color: var(--ink-navy); }
  .benefit--sleep   { left: 958px; top: 294px; font-size: 22px; color: var(--ink-brown); }
  .benefit--alkal   { left: 790px; top: 346px; font-size: 54px; color: var(--ink-navy); }
  .benefit--antiox  { left: 942px; top: 478px; font-size: 34px; color: var(--ink-green); }
  .benefit--skin    { left: 710px; top: 554px; font-size: 14px; color: var(--ink-brown); }
  .leaf {
    position: absolute;
    border-radius: 50%;
    background: radial-gradient(circle, var(--leaf-green) 0%, rgba(127,178,58,0.35) 55%, rgba(127,178,58,0) 72%);
  }
  .leaf--one   { left: 470px; top: 484px; width: 96px;  height: 108px; }
  .leaf--two   { left: 610px; top: 438px; width: 96px;  height: 114px; }
  .leaf--three { left: 758px; top: 410px; width: 110px; height: 110px; }
</style>
</head>
<body>
<main class="window-panel">
  <svg class="water-scene" role="img" aria-label="Photograph of a clear water wave with bubbles, seen at the surface" viewBox="0 0 1200 613" preserveAspectRatio="none">
    <defs>
      <linearGradient id="water-body" x1="0" y1="0" x2="0" y2="1">
        <stop offset="0" stop-color="var(--water-mid)" stop-opacity="0.55"/>
        <stop offset="0.35" stop-color="var(--water-light)"/>
        <stop offset="1" stop-color="var(--water-pale)" stop-opacity="0.4"/>
      </linearGradient>
      <linearGradient id="wave-crest" x1="0" y1="0" x2="1" y2="0">
        <stop offset="0" stop-color="var(--water-mid)"/>
        <stop offset="0.45" stop-color="var(--water-deep)"/>
        <stop offset="1" stop-color="var(--water-mid)" stop-opacity="0.7"/>
      </linearGradient>
    </defs>
    <path d="M0 150 C120 110 200 95 300 140 C420 200 560 250 700 280 C820 300 900 240 1000 220 C1080 205 1150 200 1200 210 L1200 613 L0 613 Z" fill="url(#water-body)"/>
    <path d="M0 150 C120 110 200 95 300 140 C420 200 560 250 700 280 C820 300 900 240 1000 220 C1080 205 1150 200 1200 210 L1200 250 C1120 240 1060 250 990 270 C880 310 800 320 680 300 C540 275 420 230 300 180 C200 140 100 160 0 190 Z" fill="url(#wave-crest)" opacity="0.85"/>
  </svg>

  <p class="brand brand--water">Brivelta</p>
  <p class="brand brand--cbd">Mendoli</p>

  <p class="benefit benefit--detox">entschlackend</p>
  <p class="benefit benefit--cbd">wasserlösliches CBD</p>
  <p class="benefit benefit--aging">anti-aging</p>
  <p class="benefit benefit--perform">leistungssteigernd</p>
  <p class="benefit benefit--inflam">entzündungshemmend</p>
  <p class="benefit benefit--hydrate">hydrierend</p>
  <p class="benefit benefit--sleep">schlaffördernd</p>
  <p class="benefit benefit--alkal">entsäurend</p>
  <p class="benefit benefit--antiox">antioxidativ</p>
  <p class="benefit benefit--skin">schöneres Hautbild</p>

  <div class="leaf leaf--one" role="img" aria-label="Green hemp leaf illustration"></div>
  <div class="leaf leaf--two" role="img" aria-label="Green hemp leaf illustration"></div>
  <div class="leaf leaf--three" role="img" aria-label="Green hemp leaf illustration"></div>
</main>
</body>
</html>
```